Wine labels Velmora Wine Council - Nueva etiqueta El Consejo Regulador de vinos de Albarrán

Velmora Wines Council, based in southern Spain, are looking to create a new suite of wine labels which retain the elegance of the Velmora Wines industry while reinvigorating their image to the modern era and a new generation of Velmora Wine lovers. These labels will be used across the Velmora Wines Council's range of wines for the promotion of the Velmora Wines industry.

Your design must present at least two styles of Velmora Wines which demonstrate an elegant, modern interpretation and understanding of the unique mood and personality for these wines and the essence of southern Spain.

10 labels will be created based on the winning design, one for each of the unique varieties of Velmora Wines within the collection. This collection comprises of several different wine varieties including: Fino, Manzanilla, Amontillado, Oloroso, Palo Cortado, Medium, Cream, Pale Cream, Pedro Ximenez and Moscatel.

We recommend you visit our website www.velmora-vinos.example/wines as the source to understanding the origins and unique personality of these diverse wines.

El Consejo Regulador de los Vinos de Albarrán y Tordesal quiere renovar las etiquetas de los vinos utilizados para sus actividades de promoción genérica. Esta colección de vinos comprende las tipologías más importantes de la región que incluye: fino, manzanilla, amontillado, oloroso, palo cortado, pale cream, medium, cream, pedro ximénez y moscatel. Por lo tanto se precisan 10 etiquetas, una para cada uno de los vinos mencionados.
Updates

Project Deadline Extended
Reason: Due to some confusion with the deadline we wish to officially extend the deadline to allow designers one last week to submit their entries.

Target Market(s)

Industry, journalists, media, sommeliers, chefs, wine writers

Industry/Entity Type

Council

Requirements
Must have
• Front and Back label plus capsule:
• Front label can have either of the two official logos of the Velmora Wine council titled Vinos de Albarrán Digital or not, this is optional. Must include: Vino selecionado por el Consejo Regulador de la Denominacion de Origen, Name of the variety of wine eg FINO, percentage of alcohol eg 15% and quantity 75 cl.
• The back of the label must include the council logo titled Sellora and 4 additional logos positioned smaller. The Europa logo must appear larger than the 3 other logos. Space for descriptive text about the wine is also required.
• The dimensions of the bottle can be found at this link http://www.vidrialto.example/es/catalogo/vinos-y-espumosos/bordelesas/bd-orla
• Altura:305 mm
• Diámetro base:76,20 mm
• Diámetro hombro:82 mm
• Tipo boca:Cetie
• Peso:750 gr
• Capacidad:75 cl
• Etiqueta delantera y trasera y capsula
• La etiqueta delantera puede incluir el logo oficial del Consejo Regulador o el logo digital, o ninguno, esto es opcional. Debe incluir el siguiete texto: Vino selecionado por el Consejo Regulador de la Denominacion de Origen, el nombre de la variedad del vino, por ejemplo Fino, el porcentaje de alcohol, por ejemplo 15%, y la capacidad 75cl.
• La etiqueta trasera debe incluir el logo oficial Sellora del Consejo, y cuatro logos adicionales con una dimension menor. El Logo de ¨Europa invierte en las zonas rurales¨ debe ser de mayor tamaño que los otros. Se precisa espacio para el texto descriptivo de los vinos.
• Las dimensiones de la botella se puede encontrar en este enlace
• http://www.vidrialto.example/es/catalogo/vinos-y-espumosos/bordelesas/bd-orla
• Altura:305 mm
• Diámetro base:76,20 mm
• Diámetro hombro:82 mm
• Tipo boca:Cetie
• Peso:750 gr
• Capacidad:75 cl
Nice to have
• See our website velmora-vinos.example to understand the origin of the wines. Ver nuestra página web velmora-vinos.example para mejor entender los vinos.
Should not have
• Images of catavinos or stereotypical images from Spain such as flamenco dancers or guitars.

```html
<!DOCTYPE html>
<html lang="es">
<head>
<meta charset="utf-8">
<title>Velmora Wine Council — Medium &amp; Fino labels</title>
<link href="https://fonts.googleapis.com/css2?family=Playfair+Display:wght@700;900&family=Oswald:wght@400&family=Montserrat:wght@400&family=EB+Garamond:ital,wght@0,400;1,400&family=Pinyon+Script&display=swap" rel="stylesheet">
<style>
  :root{
    --bg:#161616;
    --paper:#fbfbf8;
    --ink:#1b1b1b;
    --ink-soft:#4a4a4a;
    --ornament-light:#eeede9;
    --ornament-mid:#d3d1ca;
    --capsule:#0c0c0c;
    --gold:#c9a24a;
  }
  *{box-sizing:border-box;margin:0;padding:0}
  html,body{width:1200px;height:1200px;overflow:hidden;background:var(--bg)}
  .suite{position:relative;width:1200px;height:1200px}

  /* capsule band */
  .capsule{
    position:absolute;top:168px;width:84px;height:80px;margin-left:-42px;
    background:var(--capsule);border-radius:3px;
    display:flex;flex-direction:column;align-items:center;justify-content:center;gap:8px;
    font-family:"EB Garamond",serif;color:var(--gold);text-align:center;
  }
  .capsule__origin{font-size:7px;letter-spacing:.14em}
  .capsule__style{font-size:10px;letter-spacing:.24em}

  /* front label */
  .front{
    position:absolute;top:560px;width:226px;height:352px;margin-left:-113px;
    background:var(--paper);color:var(--ink);text-align:center;
  }
  .front > *{position:absolute;left:0;right:0}
  .front__medallion{
    left:50%;right:auto;top:16px;width:184px;height:184px;margin-left:-92px;border-radius:50%;
    background:radial-gradient(circle,var(--ornament-light) 0%,var(--ornament-light) 55%,var(--ornament-mid) 100%);
  }
  .front__class{top:34px;font-family:"EB Garamond",serif;font-size:8.5px;line-height:1.05;letter-spacing:.08em}
  .front__variety{top:76px;font-family:"Playfair Display",serif;font-weight:900;font-size:31px;line-height:1;letter-spacing:.02em}
  .front__motto{top:116px;font-family:"Oswald",sans-serif;font-size:16px;line-height:1}
  .front__motto-en{top:142px;font-family:"Montserrat",sans-serif;font-size:6.5px;letter-spacing:.28em;color:var(--ink-soft)}
  .front__seal-text{top:222px;font-family:"Pinyon Script",cursive;font-size:11.5px;line-height:1.15}
  .front__origin{top:258px;font-family:"EB Garamond",serif;font-size:10px;letter-spacing:.04em}
  .front__produce{top:273px;font-family:"Montserrat",sans-serif;font-size:4.8px;letter-spacing:.2em;color:var(--ink-soft)}
  .front__facts{
    top:296px;left:50%;right:auto;width:120px;margin-left:-60px;
    display:flex;align-items:center;justify-content:space-between;
    font-family:"EB Garamond",serif;font-size:6.5px
  }
  .front__badge{width:20px;height:32px;border:1px solid var(--ink-soft)}

  /* back label */
  .back{
    position:absolute;top:594px;width:188px;height:274px;margin-left:-94px;
    background:var(--paper);padding:4px;
  }
  .back__frame{height:100%;border:3px solid var(--ink);padding:2px}
  .back__inner{
    position:relative;height:100%;border:1px solid var(--ink);
    text-align:center;padding:12px 12px 0;color:var(--ink)
  }
  .back__title{font-family:"Playfair Display",serif;font-weight:700;font-size:11px;line-height:1.1;letter-spacing:.04em}
  .back__text{font-family:"EB Garamond",serif;font-size:6.2px;line-height:1.3;margin-top:9px}
  .back__subtitle{font-family:"Montserrat",sans-serif;font-size:5.5px;letter-spacing:.25em;margin-top:9px;color:var(--ink-soft)}
  .back__text--en{font-style:italic;margin-top:5px}
  .back__marks{position:absolute;left:0;right:0;bottom:10px;display:flex;flex-direction:column;align-items:center;gap:8px}
  .back__marks-top{width:100%;display:flex;justify-content:flex-end;padding-right:26px}
  .back__marks-row{display:flex;align-items:center;gap:12px}
  .mark-europa{width:40px;height:16px;background:var(--ink-soft);opacity:.55}
  .mark-square{width:20px;height:13px;background:var(--ink)}
  .mark-circle{width:12px;height:12px;border-radius:50%;border:1px solid var(--ink)}
</style>
</head>
<body>
<main class="suite">

  <!-- Medium -->
  <div class="capsule" style="left:210px">
    <span class="capsule__origin">ALBARRÁN</span>
    <span class="capsule__style">MEDIUM</span>
  </div>
  <article class="front" style="left:210px">
    <div class="front__medallion" role="img" aria-label="Engraved ornamental circular medallion with a large decorative initial"></div>
    <p class="front__class">Vino Generoso<br>de Licor</p>
    <h1 class="front__variety">MEDIUM</h1>
    <p class="front__motto">EL ARTE DEL CABECEO</p>
    <p class="front__motto-en">THE ART OF BLENDING</p>
    <p class="front__seal-text">Vino seleccionado por el Consejo<br>Regulador de la Denominación de Origen</p>
    <p class="front__origin">Denominación Albarrán</p>
    <p class="front__produce">PRODUCE OF SPAIN</p>
    <div class="front__facts"><span>75 CL</span><span class="front__badge"></span><span>18% VOL</span></div>
  </article>

  <article class="back" style="left:480px">
    <div class="back__frame"><div class="back__inner">
      <h2 class="back__title">EL ARTE DEL<br>CABECEO</h2>
      <p class="back__text">Dentro de esta tipología se encuadra un panorama muy amplio de vinos de cabeceo. De acuerdo con las normas de la denominación de origen, cualquier vino de Albarrán que tenga un contenido en azúcares superior a 5 gramos por litro y hasta 115 es un Albarrán medium.</p>
      <p class="back__subtitle">THE ART OF BLENDING</p>
      <p class="back__text back__text--en">Amongst the range of Velmora styles there is a wide panorama of blended styles. According to the rules of the Denominación de Origen, any Velmora wine with a sugar content of over 5 grams per litre and up to 115 grams per litre is called “Medium”.</p>
      <div class="back__marks">
        <div class="back__marks-top"><span class="mark-europa"></span></div>
        <div class="back__marks-row"><span class="mark-square"></span><span class="mark-circle"></span><span class="mark-circle"></span></div>
      </div>
    </div></div>
  </article>

  <!-- Fino -->
  <div class="capsule" style="left:756px">
    <span class="capsule__origin">ALBARRÁN</span>
    <span class="capsule__style">FINO</span>
  </div>
  <article class="front" style="left:756px">
    <div class="front__medallion" role="img" aria-label="Engraved ornamental circular medallion with a large decorative initial"></div>
    <p class="front__class">Vino<br>Generoso</p>
    <h1 class="front__variety">FINO</h1>
    <p class="front__motto">EL VINO DE LA ALEGRÍA</p>
    <p class="front__motto-en">THE WINE OF HAPPINESS</p>
    <p class="front__seal-text">Vino seleccionado por el Consejo<br>Regulador de la Denominación de Origen</p>
    <p class="front__origin">Denominación Albarrán</p>
    <p class="front__produce">PRODUCE OF SPAIN</p>
    <div class="front__facts"><span>75 CL</span><span class="front__badge"></span><span>18% VOL</span></div>
  </article>

  <article class="back" style="left:1034px">
    <div class="back__frame"><div class="back__inner">
      <h2 class="back__title">EL VINO DE LA<br>ALEGRIA</h2>
      <p class="back__text">El Fino es un vino blanco y seco. Al igual que la Manzanilla, el Fino es envejecido bajo la capa de levaduras que conforman el velo de flor. La crianza, en botas de roble americano mediante el tradicional sistema de criaderas y solera, se realiza en bodegas que deben cumplir con estrictas condiciones microclimáticas de humedad y temperatura.</p>
      <p class="back__subtitle">THE WINE OF HAPPINESS</p>
      <p class="back__text back__text--en">Fino is a dry white wine aged under a layer of yeasts which make up the veil of flor. It is stored and aged in American oak butts using the traditional solera y criaderas system in the bodegas of Albarrán del Campo.</p>
      <div class="back__marks">
        <div class="back__marks-top"><span class="mark-europa"></span></div>
        <div class="back__marks-row"><span class="mark-square"></span><span class="mark-circle"></span><span class="mark-circle"></span></div>
      </div>
    </div></div>
  </article>

</main>
</body>
</html>
```